Phuket Thailand - Rental Villa Website

I have a villa for rent in Thailand and require a website - i need to demo pictures/walk through video, local attractions, villa facilities description plus seaonal rates and online booking.

Industry/Entity Type

Rental

Coding

Coded - Design and coding required

```html
<!DOCTYPE html>
<html lang="en">
<head>
<meta charset="utf-8">
<title>Palm Cove Villas – Phuket Villa Rental</title>
<link href="https://fonts.googleapis.com/css2?family=Open+Sans:wght@400;600;700&family=Great+Vibes&display=swap" rel="stylesheet">
<style>
:root{
  --blue:#2a8fd0;
  --blue-dark:#1a78b8;
  --nav-top:#45ace2;
  --nav-bot:#1b7fc0;
  --orange:#f47b20;
  --orange-dark:#e0640c;
  --text:#666;
  --text-dark:#444;
  --line:#e2e2e2;
  --footer:#f3f3f3;
  --footer-bar:#e6e6e6;
  --social:#3d8cc4;
  --white:#fff;
}
*{box-sizing:border-box;margin:0;padding:0}
html,body{width:711px;height:1200px;overflow:hidden}
body{position:relative;background:var(--white);font-family:"Open Sans",Arial,sans-serif;color:var(--text)}
.abs{position:absolute}
.top-strip{left:0;top:0;width:711px;height:3px;background:var(--blue)}
.header{left:0;top:3px;width:711px;height:62px;background:linear-gradient(#f6f6f6,#fff)}
.brand{left:58px;top:22px;display:flex;align-items:center;gap:7px}
.brand-mark{width:22px;height:22px;background:var(--orange);border-radius:3px}
.brand-name{font-size:17px;font-weight:400;color:#555}
.contact{top:28px;display:flex;align-items:center;gap:5px;font-size:6.6px;color:#555}
.contact b{font-weight:400;color:var(--blue)}
.contact-icon{width:19px;height:19px;border-radius:50%;background:var(--orange);display:flex;align-items:center;justify-content:center}
.nav{left:0;top:65px;width:711px;height:23px;background:linear-gradient(var(--nav-top),var(--nav-bot));border-top:1px solid #7cc4ec}
.nav-item{top:0;height:23px;display:flex;align-items:center;justify-content:center;font-size:6.4px;color:var(--white);border-right:1px solid rgba(0,0,0,.12);text-transform:uppercase}
.nav-item.active{background:linear-gradient(#ff9440,var(--orange-dark))}
.hero{left:58px;top:100px;width:595px;height:211px;background:linear-gradient(160deg,#7a8a76 0%,#5f6468 35%,#8a6e62 60%,#6e5a52 100%)}
.hero-title{left:28px;top:104px;font-family:"Great Vibes",cursive;font-size:25px;line-height:22px;color:var(--white);text-shadow:0 1px 3px rgba(0,0,0,.6)}
.hero-caption{left:0;bottom:0;width:595px;height:35px;background:rgba(20,20,20,.75);font-size:9.2px;color:var(--white);padding:11px 16px;text-transform:uppercase}
.hero-arrows{right:10px;top:12px;display:flex;gap:2px}
.arrow-btn{width:12px;height:12px;background:rgba(255,255,255,.15);border:1px solid rgba(255,255,255,.2)}
.section-title{font-size:8.6px;font-weight:700;color:var(--blue);text-transform:uppercase}
.intro{left:58px;top:349px;width:595px;font-size:6.2px;line-height:14.5px;color:var(--text)}
.rule{left:58px;top:428px;width:595px;height:1px;background:var(--line)}
.pager{display:flex;gap:1px}
.pager span{width:11px;height:10px;background:#e8e8e8;border:1px solid #ddd}
.attraction{top:441px;width:110px}
.attraction-photo{width:110px;height:77px;border-radius:2px}
.attraction-head{display:flex;justify-content:space-between;align-items:center;margin-top:6px;font-size:7.6px;color:var(--blue)}
.rated{font-size:5.4px;color:#777}
.rated em{font-style:normal;color:var(--orange);font-size:6px;letter-spacing:-.3px}
.loc{display:flex;align-items:center;gap:3px;font-size:6.4px;color:#777;margin-top:4px}
.attraction-divider{height:1px;background:var(--line);margin:6px 0 5px}
.features{font-size:6.2px;line-height:11px;color:var(--blue)}
.buy{display:flex;align-items:center;justify-content:center;margin-top:6px;width:60px;height:18px;background:linear-gradient(#ff9440,var(--orange-dark));color:var(--white);font-size:5.6px;font-weight:700;border-radius:2px}
.video{left:58px;top:653px;width:228px;height:155px}
.video-frame{width:228px;height:144px;background:linear-gradient(180deg,#9cc3e6 0%,#6f93b8 30%,#3c4c58 55%,#2a2a28 100%)}
.video-bar{width:228px;height:11px;background:linear-gradient(#f4f4f4,#d6d6d6);border:1px solid #bbb;display:flex;align-items:center;gap:4px;padding:0 4px;font-size:4.6px;color:#333}
.video-track{flex:1;height:3px;background:#aaa;border-radius:2px}
.news-item{left:318px;width:335px}
.news-photo{left:0;top:0;width:88px;height:59px}
.news-title{left:104px;top:0;font-size:7.4px;color:var(--blue)}
.news-date{left:104px;top:16px;font-size:6px;color:var(--orange)}
.news-body{left:104px;top:30px;width:225px;font-size:5.8px;line-height:14px;color:#777}
.tab{top:834px;height:24px;display:flex;align-items:center;justify-content:center;font-size:6.6px;font-weight:600;color:var(--white);text-transform:uppercase}
.tab-recent{left:58px;width:94px;background:linear-gradient(#ff9440,var(--orange-dark))}
.tab-rates{left:153px;width:93px;background:linear-gradient(#4cb0e4,var(--blue-dark))}
.tab-panel{left:58px;top:858px;width:595px;height:137px;border:1px solid #e0e0e0;background:#fafafa}
.villa-card{top:872px;width:104px;height:109px;background:var(--white);border:1px solid #e4e4e4;border-radius:2px;padding:4px}
.villa-photo{width:96px;height:68px}
.villa-name{font-size:6.2px;color:var(--blue);margin:8px 0 0 6px}
.villa-card .loc{margin:5px 0 0 6px}
.footer{left:0;top:1014px;width:711px;height:158px;background:var(--footer)}
.footer-col{top:1034px;font-family:Arial,sans-serif}
.footer-col h4{font-family:"Open Sans",sans-serif;font-size:6.4px;font-weight:700;color:var(--blue);text-transform:uppercase;margin-bottom:9px}
.footer-col li{list-style:none;font-size:6px;line-height:14.2px;color:#555}
.footer-col p{font-size:6px;line-height:14.2px;color:#555;display:flex;align-items:center;gap:4px}
.footer-col p.strong{color:var(--blue-dark)}
.social{display:flex;align-items:center;gap:3px;font-size:5.6px;color:#555;height:21px}
.social i{width:15px;height:15px;border-radius:50%;display:block;background:var(--social)}
.footer-brand{left:566px;top:1064px;display:flex;flex-direction:column;align-items:center;gap:6px}
.footer-brand-name{font-size:11px;color:#666}
.footer-bar{left:0;top:1172px;width:711px;height:28px;background:var(--footer-bar);display:flex;align-items:center;justify-content:center;font-family:Arial,sans-serif;font-size:5.8px;color:#555}
</style>
</head>
<body>

<div class="abs top-strip"></div>
<header class="abs header"></header>

<div class="abs brand">
  <span class="brand-mark"></span>
  <span class="brand-name">Palm Cove Villas</span>
</div>

<div class="abs contact" style="left:398px">
  <span class="contact-icon"><svg width="9" height="9" viewBox="0 0 24 24"><path fill="#fff" d="M6.6 10.8a15 15 0 0 0 6.6 6.6l2.2-2.2c.3-.3.7-.4 1-.2 1.1.4 2.3.6 3.6.6.6 0 1 .4 1 1V20c0 .6-.4 1-1 1A17 17 0 0 1 3 4c0-.6.4-1 1-1h3.5c.6 0 1 .4 1 1 0 1.3.2 2.5.6 3.6.1.3 0 .7-.2 1z"/></svg></span>
  <span>CALL US : <b>(0123) 555 014</b></span>
</div>
<div class="abs contact" style="left:511px">
  <span class="contact-icon"><svg width="9" height="9" viewBox="0 0 24 24"><path fill="#fff" d="M2 5h20v14H2z"/><path fill="none" stroke="#f47b20" stroke-width="2" d="M2 6l10 7 10-7"/></svg></span>
  <span>EMAIL US : <b>stay@palmcovevillas.example</b></span>
</div>

<nav class="abs nav">
  <div class="abs nav-item active" style="left:60px;width:56px">Home</div>
  <div class="abs nav-item" style="left:116px;width:78px">About Us</div>
  <div class="abs nav-item" style="left:194px;width:70px">Services</div>
  <div class="abs nav-item" style="left:264px;width:62px">Villas</div>
  <div class="abs nav-item" style="left:326px;width:66px">Videos</div>
  <div class="abs nav-item" style="left:392px;width:70px">Gallery</div>
  <div class="abs nav-item" style="left:462px;width:58px">News</div>
  <div class="abs nav-item" style="left:520px;width:82px">Contact Us</div>
</nav>

<section class="abs hero" role="img" aria-label="Photo of a villa rooftop with tiled roof against green hillside">
  <div class="abs hero-title">Villa rental service in Phuket,<br>it is in Thailand.</div>
  <div class="abs hero-caption">Lorem Ipsum has been the industry's standard dummy text ever since the 1500s, when an unknown...
    <div class="abs hero-arrows"><span class="arrow-btn"></span><span class="arrow-btn"></span></div>
  </div>
</section>

<h2 class="abs section-title" style="left:58px;top:333px">Welcome to Palm Cove Villas</h2>
<p class="abs intro">Lorem Ipsum is simply dummy text of the printing and typesetting industry. Lorem Ipsum has been the industry's standard dummy text ever since the 1500s, when an unknown printer took a galley of type and scrambled it to make a type specimen book. It has survived not only five centuries, but also the leap into electronic typesetting, remaining essentially unchanged. It was popularised in the 1960s with the release of Letraset sheets containing...</p>

<h2 class="abs section-title" style="left:58px;top:409px">Local Attractions</h2>
<div class="abs pager" style="left:630px;top:412px"><span></span><span></span></div>
<div class="abs rule"></div>

<div class="abs attraction" style="left:58px">
  <div class="attraction-photo" role="img" aria-label="Photo of a villa bedroom" style="background:linear-gradient(135deg,#5a4a44,#b8b0a8 55%,#7d8a8e)"></div>
  <div class="attraction-head"><span>Facility</span><span class="rated">Rated <em>★★★★☆</em></span></div>
  <div class="loc"><svg width="5" height="7" viewBox="0 0 10 14"><path fill="#777" d="M5 0a5 5 0 0 0-5 5c0 4 5 9 5 9s5-5 5-9a5 5 0 0 0-5-5zm0 7a2 2 0 1 1 0-4 2 2 0 0 1 0 4z"/></svg>lorem ipsum</div>
  <div class="attraction-divider"></div>
  <div class="features">2 Bed Rooms,<br>2 Attached Bathrooms,<br>Swimming pool</div>
  <div class="buy">BUY NOW</div>
</div>
<div class="abs attraction" style="left:180px">
  <div class="attraction-photo" role="img" aria-label="Photo of a timber pavilion overlooking hills" style="background:linear-gradient(180deg,#c9cfd4,#6b6258 55%,#8d9a86)"></div>
  <div class="attraction-head"><span>Facility</span><span class="rated">Rated <em>★★★★☆</em></span></div>
  <div class="loc"><svg width="5" height="7" viewBox="0 0 10 14"><path fill="#777" d="M5 0a5 5 0 0 0-5 5c0 4 5 9 5 9s5-5 5-9a5 5 0 0 0-5-5zm0 7a2 2 0 1 1 0-4 2 2 0 0 1 0 4z"/></svg>lorem ipsum</div>
  <div class="attraction-divider"></div>
  <div class="features">2 Bed Rooms,<br>2 Attached Bathrooms,<br>Swimming pool</div>
  <div class="buy">BUY NOW</div>
</div>
<div class="abs attraction" style="left:302px">
  <div class="attraction-photo" role="img" aria-label="Photo of a villa with tiled roof among trees" style="background:linear-gradient(150deg,#5e7452,#8a8e88 45%,#7a5e52)"></div>
  <div class="attraction-head"><span>Facility</span><span class="rated">Rated <em>★★★★☆</em></span></div>
  <div class="loc"><svg width="5" height="7" viewBox="0 0 10 14"><path fill="#777" d="M5 0a5 5 0 0 0-5 5c0 4 5 9 5 9s5-5 5-9a5 5 0 0 0-5-5zm0 7a2 2 0 1 1 0-4 2 2 0 0 1 0 4z"/></svg>lorem ipsum</div>
  <div class="attraction-divider"></div>
  <div class="features">2 Bed Rooms,<br>2 Attached Bathrooms,<br>Swimming pool</div>
  <div class="buy">BUY NOW</div>
</div>
<div class="abs attraction" style="left:422px">
  <div class="attraction-photo" role="img" aria-label="Photo of an open timber sala with sea view" style="background:linear-gradient(180deg,#6a4a3a,#a89a86 50%,#5a5448)"></div>
  <div class="attraction-head"><span>Facility</span><span class="rated">Rated <em>★★★★☆</em></span></div>
  <div class="loc"><svg width="5" height="7" viewBox="0 0 10 14"><path fill="#777" d="M5 0a5 5 0 0 0-5 5c0 4 5 9 5 9s5-5 5-9a5 5 0 0 0-5-5zm0 7a2 2 0 1 1 0-4 2 2 0 0 1 0 4z"/></svg>lorem ipsum</div>
  <div class="attraction-divider"></div>
  <div class="features">2 Bed Rooms,<br>2 Attached Bathrooms,<br>Swimming pool</div>
  <div class="buy">BUY NOW</div>
</div>
<div class="abs attraction" style="left:543px">
  <div class="attraction-photo" role="img" aria-label="Photo of an infinity pool facing the sea" style="background:linear-gradient(180deg,#c8d4dc,#8a9a90 40%,#6a9e9a 70%,#4e7e80)"></div>
  <div class="attraction-head"><span>Facility</span><span class="rated">Rated <em>★★★★☆</em></span></div>
  <div class="loc"><svg width="5" height="7" viewBox="0 0 10 14"><path fill="#777" d="M5 0a5 5 0 0 0-5 5c0 4 5 9 5 9s5-5 5-9a5 5 0 0 0-5-5zm0 7a2 2 0 1 1 0-4 2 2 0 0 1 0 4z"/></svg>lorem ipsum</div>
  <div class="attraction-divider"></div>
  <div class="features">2 Bed Rooms,<br>2 Attached Bathrooms,<br>Swimming pool</div>
  <div class="buy">BUY NOW</div>
</div>

<div class="abs video">
  <div class="video-frame" role="img" aria-label="Villa walk-through video: thatched beach pavilion with loungers and ocean view">
    <svg width="228" height="144" viewBox="0 0 228 144"><circle cx="114" cy="72" r="15" fill="none" stroke="#fff" stroke-width="2.5"/><path d="M109 63l13 9-13 9z" fill="#fff"/></svg>
  </div>
  <div class="video-bar"><span>▶</span><span>00:00</span><span class="video-track"></span><span>00:00</span><span>◀▮</span><span>⤢</span></div>
</div>

<h2 class="abs section-title" style="left:318px;top:651px">Latest News</h2>
<div class="abs pager" style="left:630px;top:650px"><span></span><span></span></div>

<article class="abs news-item" style="top:673px;height:60px">
  <div class="abs news-photo" role="img" aria-label="Photo of a modern villa and pool at dusk" style="background:linear-gradient(180deg,#2a5a9a,#4a7cb8 45%,#1a2a4a)"></div>
  <div class="abs news-title">Lorem Ipsum is simply dummy text of the printing.</div>
  <div class="abs news-date">Posted on 27 January 2015</div>
  <p class="abs news-body">Lorem Ipsum is simply dummy text of the printing and typesetting indus try. Lorem Ipsum has been the industry's...</p>
</article>
<article class="abs news-item" style="top:748px;height:60px">
  <div class="abs news-photo" role="img" aria-label="Photo of a happy family on holiday" style="background:linear-gradient(135deg,#e6e0d8,#c9a48a 50%,#8a9ab4)"></div>
  <div class="abs news-title">Lorem Ipsum is simply dummy text of the printing.</div>
  <div class="abs news-date">Posted on 27 January 2015</div>
  <p class="abs news-body">Lorem Ipsum is simply dummy text of the printing and typesetting indus try. Lorem Ipsum has been the industry's...</p>
</article>

<div class="abs tab tab-recent">Recent Villas</div>
<div class="abs tab tab-rates">Seasonal Rates</div>
<div class="abs tab-panel"></div>

<div class="abs villa-card" style="left:73px">
  <div class="villa-photo" role="img" aria-label="Photo of a villa pool at twilight" style="background:linear-gradient(180deg,#1e4e9e,#3a6ab0 50%,#a07030 75%,#1a2a5a)"></div>
  <div class="villa-name">Lorem Ipsum is simply</div>
  <div class="loc"><svg width="5" height="7" viewBox="0 0 10 14"><path fill="#777" d="M5 0a5 5 0 0 0-5 5c0 4 5 9 5 9s5-5 5-9a5 5 0 0 0-5-5zm0 7a2 2 0 1 1 0-4 2 2 0 0 1 0 4z"/></svg>lorem ipsum</div>
</div>
<div class="abs villa-card" style="left:189px">
  <div class="villa-photo" role="img" aria-label="Photo of a lit villa exterior at night" style="background:linear-gradient(180deg,#1a2238,#4a3a2a 45%,#c08a40 70%,#2a2a2a)"></div>
  <div class="villa-name">Lorem Ipsum is simply</div>
  <div class="loc"><svg width="5" height="7" viewBox="0 0 10 14"><path fill="#777" d="M5 0a5 5 0 0 0-5 5c0 4 5 9 5 9s5-5 5-9a5 5 0 0 0-5-5zm0 7a2 2 0 1 1 0-4 2 2 0 0 1 0 4z"/></svg>lorem ipsum</div>
</div>
<div class="abs villa-card" style="left:304px">
  <div class="villa-photo" role="img" aria-label="Photo of a modern villa reflected in a pool" style="background:linear-gradient(180deg,#3a5a8a,#8a90a0 45%,#2a3a5a 75%,#1a2a3a)"></div>
  <div class="villa-name">Lorem Ipsum is simply</div>
  <div class="loc"><svg width="5" height="7" viewBox="0 0 10 14"><path fill="#777" d="M5 0a5 5 0 0 0-5 5c0 4 5 9 5 9s5-5 5-9a5 5 0 0 0-5-5zm0 7a2 2 0 1 1 0-4 2 2 0 0 1 0 4z"/></svg>lorem ipsum</div>
</div>
<div class="abs villa-card" style="left:419px">
  <div class="villa-photo" role="img" aria-label="Photo of a thatched beach pavilion by the sea" style="background:linear-gradient(180deg,#4a8ad0,#a8c8e8 35%,#4a9ab0 60%,#3a2a22)"></div>
  <div class="villa-name">Lorem Ipsum is simply</div>
  <div class="loc"><svg width="5" height="7" viewBox="0 0 10 14"><path fill="#777" d="M5 0a5 5 0 0 0-5 5c0 4 5 9 5 9s5-5 5-9a5 5 0 0 0-5-5zm0 7a2 2 0 1 1 0-4 2 2 0 0 1 0 4z"/></svg>lorem ipsum</div>
</div>
<div class="abs villa-card" style="left:534px">
  <div class="villa-photo" role="img" aria-label="Photo of a palm-framed seaside terrace" style="background:linear-gradient(160deg,#1a3a2a,#3a6a9a 40%,#6aa0d0 65%,#c8b898)"></div>
  <div class="villa-name">Lorem Ipsum is simply</div>
  <div class="loc"><svg width="5" height="7" viewBox="0 0 10 14"><path fill="#777" d="M5 0a5 5 0 0 0-5 5c0 4 5 9 5 9s5-5 5-9a5 5 0 0 0-5-5zm0 7a2 2 0 1 1 0-4 2 2 0 0 1 0 4z"/></svg>lorem ipsum</div>
</div>

<footer class="abs footer"></footer>

<div class="abs footer-col" style="left:74px">
  <h4>Welcome</h4>
  <ul><li>Home</li><li>About Us</li><li>Services</li><li>Villas</li><li>Videos</li><li>Gallery</li><li>News</li><li>Contact us</li></ul>
</div>
<div class="abs footer-col" style="left:171px">
  <h4>Information</h4>
  <ul><li>Terms &amp; Conditions</li><li>Privacy policy</li><li>Disclaimer</li><li>Sitemap</li></ul>
</div>
<div class="abs footer-col" style="left:289px">
  <h4>Contact Info</h4>
  <p class="strong">Villa rental service in Phuket</p>
  <p>120 STreet name, City name,</p>
  <p>Country name : 2365233</p>
  <p><svg width="6" height="6" viewBox="0 0 24 24"><path fill="#555" d="M6.6 10.8a15 15 0 0 0 6.6 6.6l2.2-2.2c.3-.3.7-.4 1-.2 1.1.4 2.3.6 3.6.6.6 0 1 .4 1 1V20c0 .6-.4 1-1 1A17 17 0 0 1 3 4c0-.6.4-1 1-1h3.5c.6 0 1 .4 1 1 0 1.3.2 2.5.6 3.6.1.3 0 .7-.2 1z"/></svg>(0123) 555 014</p>
  <p><svg width="6" height="5" viewBox="0 0 24 18"><rect width="24" height="18" fill="#555"/><path d="M0 1l12 8 12-8" fill="none" stroke="#f3f3f3" stroke-width="2"/></svg>stay@palmcovevillas.example</p>
</div>
<div class="abs footer-col" style="left:452px">
  <h4>Follow Us</h4>
  <div class="social"><i></i>: Community</div>
  <div class="social"><i></i>: Updates</div>
  <div class="social"><i></i>: Network</div>
  <div class="social"><i></i>: Photo board</div>
</div>

<div class="abs footer-brand">
  <span class="brand-mark" style="width:16px;height:16px"></span>
  <span class="footer-brand-name">Palm Cove Villas</span>
</div>

<div class="abs footer-bar">© 2015. Palm Cove Villas. All Rights Reserved.</div>

</body>
</html>
```